Velmi Corporate Website for technological company

We need a modern website to promote our product and services.
You can found the actually website at the address: www.velmi-example.ch

We are a new company for B2B market. We would like do show our high precision and innovation capability.

we need a section were is possible to easily upload "news" and documents for our customers.

Target Market(s)

B2B services in the industry market

Industry/Entity Type

It Company

Coding

Coded - Design and coding required

Number of Pages Required

5+ page

Font styles to use
Other font styles liked:
• We accept propositions

Requirements
Must have
• Easy to maintain
• Presentation of the Velmi company
• Presentation of Velmi services and products
• The customer can download our ducumentation
Nice to have
• Sexy and modern

```html
<!DOCTYPE html>
<html lang="en">
<head>
<meta charset="utf-8">
<title>Velmi Sàrl – Intelligent Motion</title>
<link rel="stylesheet" href="https://fonts.googleapis.com/css2?family=Raleway:wght@200;300;400;500;600;700&family=Open+Sans:wght@400;600;700&display=swap">
<style>
:root{
  --gold:#b0a77a;
  --gold-dark:#8f875d;
  --navy:#1d3a5c;
  --ink:#2b2b2b;
  --text:#555;
  --light:#ededee;
  --white:#fff;
  --dark:#1b1c1e;
  --hero-a:#2c4764;
  --hero-b:#8a9bb0;
}
*{box-sizing:border-box;margin:0;padding:0}
html,body{width:1200px;height:4539px;overflow:hidden}
body{font-family:"Open Sans",Arial,sans-serif;color:var(--text);background:var(--white);position:relative}
section,header,footer{position:absolute;left:0;width:1200px;overflow:hidden}
.abs{position:absolute}
.center{left:0;width:1200px;text-align:center}
.section-title{position:absolute;left:0;width:1200px;text-align:center;font-family:"Raleway",sans-serif;font-weight:300;font-size:34px;letter-spacing:1px;color:var(--ink)}
.section-title::after{content:"";display:block;width:70px;height:3px;background:var(--navy);margin:12px auto 0}
.on-dark .section-title{color:var(--white)}
.on-dark .section-title::after{background:var(--gold)}
.btn{position:absolute;background:var(--gold);color:#2a2a2a;font-family:"Raleway",sans-serif;font-weight:600;font-size:17px;text-align:center;letter-spacing:.5px}

/* Hero */
.hero{top:0;height:597px;background:linear-gradient(180deg,#566e88 0%,var(--hero-b) 35%,var(--hero-a) 75%,#20334a 100%)}
.hero-photo{position:absolute;inset:0;background:radial-gradient(ellipse at 30% 20%,rgba(220,225,232,.55),transparent 55%),radial-gradient(ellipse at 80% 80%,rgba(10,20,35,.5),transparent 60%)}
.topbar{position:absolute;top:0;left:0;width:1200px;height:72px;background:rgba(15,18,22,.85)}
.logo{position:absolute;left:140px;top:10px;height:52px;display:flex;align-items:center;gap:10px;background:var(--white);padding:0 16px}
.logo-mark{width:26px;height:26px;border-radius:50%;background:var(--gold)}
.logo-name{font-family:"Raleway",sans-serif;font-weight:700;font-size:26px;color:var(--ink)}
.nav{position:absolute;right:133px;top:17px;display:flex;gap:4px}
.nav a{font-family:"Open Sans",sans-serif;font-size:15px;color:var(--white);text-decoration:none;padding:7px 11px}
.nav a.active{background:var(--gold);color:#222}
.hero-rule{position:absolute;left:167px;width:878px;height:3px;background:var(--gold)}
.hero-line1{top:228px;font-family:"Raleway",sans-serif;font-weight:300;font-size:50px;color:var(--white);letter-spacing:1px}
.hero-line2{top:272px;font-family:"Raleway",sans-serif;font-weight:400;font-size:50px;color:var(--white);letter-spacing:1px}

/* How it work */
.how{top:597px;height:403px;background:var(--light)}
.step{position:absolute;width:340px;text-align:center}
.step h3{font-family:"Raleway",sans-serif;font-weight:600;font-size:21px;color:var(--navy);margin-top:10px}
.step ul{list-style:none;margin-top:10px}
.step li{font-size:12.5px;color:#555;line-height:29px}
.step li::before{content:"";display:inline-block;width:8px;height:8px;background:var(--navy);margin-right:8px;vertical-align:middle;border-radius:1px}

/* Cards */
.services{top:1000px;height:703px;background:#fbfbfb}
.card{position:absolute;background:var(--white);border:1px solid #d8d8d8;box-shadow:0 1px 3px rgba(0,0,0,.08)}
.card-media{position:absolute;left:8px;right:8px;top:8px}
.card h3{position:absolute;left:0;right:0;text-align:center;font-family:"Raleway",sans-serif;font-weight:600;font-size:17px;color:var(--ink)}
.card p{position:absolute;left:22px;right:22px;text-align:center;font-size:12.5px;line-height:20px;color:#555}
.slider{position:absolute;left:297px;width:606px;height:1px;background:#9aa7b6}
.arrows{position:absolute;left:565px;display:flex}
.arrows span{width:35px;height:33px;display:flex;align-items:center;justify-content:center;font-size:18px;font-weight:700}
.arrows .prev{background:var(--gold-dark);color:#222}
.arrows .next{background:var(--gold);color:#222}

/* Testimonial */
.client{top:1703px;height:676px;background:radial-gradient(ellipse at 50% 40%,#2a2823,#141414 70%)}
.avatar{position:absolute;left:491px;top:151px;width:218px;height:218px;border-radius:50%;border:6px solid #e9eef3;background:radial-gradient(circle at 50% 40%,#d8b9a0,#7aa6c6 70%)}
.role{top:410px;font-size:14px;letter-spacing:1px;color:var(--gold)}
.quote{left:190px;width:820px;top:462px;text-align:center;font-size:12.5px;line-height:22px;color:#e4e4e4}
.qmark{position:absolute;font-family:Georgia,serif;font-size:90px;line-height:1;color:var(--gold)}

/* Product */
.product{top:2379px;height:718px;background:linear-gradient(180deg,#f4f4f4,#e9e9e9 60%,#f2f2f2)}
.card .sub{position:absolute;left:0;right:0;text-align:center;font-size:10.5px;font-weight:700;color:var(--ink);text-transform:uppercase}
.card h3.name{font-family:"Raleway",sans-serif;font-weight:700;font-size:24px;color:var(--ink)}

/* Team */
.team{top:3097px;height:342px;background:linear-gradient(180deg,#2c2c2e,#1a1a1b 50%,#333 100%)}
.stat{position:absolute;width:200px;text-align:center;color:var(--white)}
.stat .num{font-family:"Raleway",sans-serif;font-weight:200;font-size:48px;line-height:1;margin-top:12px}
.stat .label{font-family:"Raleway",sans-serif;font-size:22px;color:#e7e2cc}

/* News & docs */
.news{top:3439px;height:415px;background:var(--light)}
.col-title{position:absolute;font-family:"Raleway",sans-serif;font-weight:400;font-size:30px;color:var(--ink);letter-spacing:.5px}
.col-rule{position:absolute;height:2px;background:var(--navy)}
.list-box{position:absolute;width:456px;height:303px;top:82px;background:var(--white);border:1px solid #dcdcdc}
.item{position:absolute;left:8px;width:440px;height:110px}
.item .thumb{position:absolute;left:0;top:0;width:104px;height:98px}
.item h4{position:absolute;left:114px;top:0;font-family:"Open Sans",sans-serif;font-weight:700;font-size:14px;color:var(--navy)}
.item p{position:absolute;left:114px;top:24px;right:6px;font-size:11px;line-height:15px;color:#555}
.item .more{position:absolute;left:114px;top:86px;font-size:9.5px;font-weight:700;color:var(--ink);letter-spacing:.5px}

/* Contact */
.contact{top:3854px;height:625px;background:linear-gradient(90deg,#26282b 0%,#2f3134 55%,#4a4a4a 100%)}
.contact .h{top:38px;font-family:"Raleway",sans-serif;font-weight:500;font-size:32px;color:var(--white)}
.field{position:absolute;left:133px;width:503px;border-bottom:1px solid #9a9a9a;font-size:12px;font-weight:600;color:#ddd;padding-bottom:8px}
.divider{position:absolute;left:703px;top:180px;width:1px;height:270px;background:#777}
.info-icon{position:absolute;left:767px}
.info{position:absolute;left:767px;font-size:19px;color:#e9e9e9}

footer{top:4479px;height:60px;background:#161617;border-top:1px solid #333}
.copy{position:absolute;left:133px;top:20px;font-size:13px;color:#d4d4d4}
.social{position:absolute;right:135px;top:24px;display:flex;gap:10px}
.social span{width:11px;height:11px;border-radius:50%;background:#b6b6b6}
</style>
</head>
<body>

<header class="hero">
  <div class="hero-photo" role="img" aria-label="Photo of a technician handling an electronic circuit board in cool blue light"></div>
  <div class="topbar">
    <div class="logo"><span class="logo-mark"></span><span class="logo-name">Velmi Sàrl</span></div>
    <nav class="nav">
      <a class="active">Home</a><a>Services</a><a>Products</a><a>Examples</a><a>Download</a><a>Contacts</a>
    </nav>
  </div>
  <div class="hero-rule" style="top:216px"></div>
  <div class="abs center hero-line1">INTELLIGENT MOTION</div>
  <div class="abs center hero-line2">WE SOLVE THAT</div>
  <div class="hero-rule" style="top:330px"></div>
  <div class="btn" style="left:485px;top:342px;width:230px;height:44px;line-height:44px">GET STARTED</div>
</header>

<section class="how">
  <h2 class="section-title" style="top:38px">HOW TI WORK</h2>
  <div class="step" style="left:80px;top:145px">
    <svg width="70" height="78" viewBox="0 0 70 78"><polygon points="35,2 68,20 68,58 35,76 2,58 2,20" fill="var(--navy)"/><circle cx="35" cy="34" r="10" fill="none" stroke="#fff" stroke-width="3"/><rect x="31" y="45" width="8" height="8" fill="#fff"/></svg>
    <h3>IDEAS</h3>
    <ul><li>Qualified native speakers &amp; professionals</li><li>More than 20 areas of expertise</li><li>Over 98% client satisfaction rate</li></ul>
  </div>
  <div class="step" style="left:427px;top:145px">
    <svg width="70" height="78" viewBox="0 0 70 78"><polygon points="35,2 68,20 68,58 35,76 2,58 2,20" fill="var(--navy)"/><path d="M24 46 L42 28 M40 26 l6 6" stroke="#fff" stroke-width="4" stroke-linecap="round"/></svg>
    <h3>WE WORK</h3>
    <ul><li>It is cents pricing</li><li>From $0.06 to $0.40 per word</li><li>12 hour average turnaround</li></ul>
  </div>
  <div class="step" style="left:778px;top:145px">
    <svg width="70" height="78" viewBox="0 0 70 78"><polygon points="35,2 68,20 68,58 35,76 2,58 2,20" fill="var(--navy)"/><rect x="23" y="26" width="24" height="18" fill="none" stroke="#fff" stroke-width="3"/><rect x="29" y="48" width="12" height="4" fill="#fff"/></svg>
    <h3>NEW TECHNOLOGY</h3>
    <ul><li>Order online 24/7</li><li>Any format (doc, xls, etc.)</li><li>Available in API, MS Office, Wordpress</li></ul>
  </div>
</section>

<section class="services">
  <h2 class="section-title" style="top:36px">OUR SERVICES</h2>
  <div class="card" style="left:133px;top:124px;width:282px;height:476px">
    <div class="card-media" style="height:176px;background:linear-gradient(135deg,#e9e9e9,#9c9c9c)" role="img" aria-label="Illustration of a robotic gripper mechanism"></div>
    <h3 style="top:206px">VELMI SERVICES</h3>
    <p style="top:236px">Lorem Ipsum is simply dummy text of the printing and typesetting industry. Lorem Ipsum has been the industry's standard dummy text ever since the 1500s, when an unknown printer took a galley of type and scrambled it to make a type specimen book. It has survived not.Lorem Ipsum is simply dummy text.</p>
    <div class="btn" style="left:25px;top:412px;width:232px;height:48px;line-height:48px">READ MORE</div>
  </div>
  <div class="card" style="left:457px;top:124px;width:283px;height:476px">
    <div class="card-media" style="height:176px;background:linear-gradient(135deg,#f2f6fb,#b9cbe2)" role="img" aria-label="Blue technical drawing of mechanical simulation schematics"></div>
    <h3 style="top:206px">SIMULATION AND MODELING</h3>
    <p style="top:236px">Lorem Ipsum is simply dummy text of the printing and typesetting industry. Lorem Ipsum has been the industry's standard dummy text ever since the 1500s, when an unknown printer took a galley of type and scrambled it to make a type specimen book. It has survived not.Lorem Ipsum is simply dummy text.</p>
    <div class="btn" style="left:25px;top:412px;width:232px;height:48px;line-height:48px">READ MORE</div>
  </div>
  <div class="card" style="left:782px;top:124px;width:282px;height:476px">
    <div class="card-media" style="height:176px;background:linear-gradient(135deg,#6b6b6b,#1e1e1e)" role="img" aria-label="Close-up photo of electronic components on a circuit board"></div>
    <h3 style="top:206px">ELECTRONICS</h3>
    <p style="top:236px">Lorem Ipsum is simply dummy text of the printing and typesetting industry. Lorem Ipsum has been the industry's standard dummy text ever since the 1500s, when an unknown printer took a galley of type and scrambled it to make a type specimen book. It has survived not.Lorem Ipsum is simply dummy text.</p>
    <div class="btn" style="left:25px;top:412px;width:232px;height:48px;line-height:48px">READ MORE</div>
  </div>
  <div class="slider" style="top:654px"></div>
  <div class="arrows" style="top:638px"><span class="prev">‹</span><span class="next">›</span></div>
</section>

<section class="client on-dark" role="img" aria-label="Dark blurred office photo background">
  <h2 class="section-title" style="top:50px">OUR CLIENT SAYS</h2>
  <div class="avatar" role="img" aria-label="Portrait photo of the client"></div>
  <div class="abs center role">JOURNALIST</div>
  <div class="qmark" style="left:150px;top:440px">“</div>
  <p class="abs quote">Lorem Ipsum is simply dummy text of the printing and typesetting industry. Lorem Ipsum has been the industry's standard dummy text ever since the 1500s, when an unknown printer took a galley of type and scrambled it to make a type specimen book. It has survived not only five centuries.</p>
  <div class="qmark" style="left:1002px;top:480px">”</div>
  <div class="slider" style="top:590px;background:#888"></div>
  <div class="arrows" style="top:574px"><span class="prev">‹</span><span class="next" style="background:#4a4535">›</span></div>
</section>

<section class="product">
  <h2 class="section-title" style="top:34px">OUR PRODUCT</h2>
  <div class="card" style="left:133px;top:124px;width:282px;height:452px">
    <div class="card-media" style="height:127px;background:linear-gradient(135deg,#c9d6c6,#3f6a4a)" role="img" aria-label="Photo of the Kestrel motor controller board"></div>
    <h3 class="name" style="top:148px">KESTREL</h3>
    <div class="sub" style="top:182px">Intelligent control for electric motors</div>
    <p style="top:206px">Lorem Ipsum is simply dummy text of the printing and typesetting industry. Lorem Ipsum has been the industry's standard dummy text ever since the 1500s, when an unknown printer took a galley of type and scrambled it to make a type specimen book. It has survived not only five centuries, but also the leap into electronic type-setting, remaining essentially unchanged.</p>
    <div class="btn" style="left:25px;top:406px;width:232px;height:42px;line-height:42px">READ MORE</div>
  </div>
  <div class="card" style="left:457px;top:124px;width:283px;height:452px">
    <div class="card-media" style="height:127px;background:linear-gradient(135deg,#d9dccf,#35573c)" role="img" aria-label="Photo of the Tessa multi-axis controller board"></div>
    <h3 class="name" style="top:148px">TESSA</h3>
    <div class="sub" style="top:182px">Le contrôleur intelligent multi-axes</div>
    <p style="top:206px">Lorem Ipsum is simply dummy text of the printing and typesetting industry. Lorem Ipsum has been the industry's standard dummy text ever since the 1500s, when an unknown printer took a galley of type and scrambled it to make a type specimen book. It has survived not only five centuries, but also the leap into electronic type-setting, remaining essentially unchanged.</p>
    <div class="btn" style="left:25px;top:406px;width:232px;height:42px;line-height:42px">READ MORE</div>
  </div>
  <div class="card" style="left:782px;top:124px;width:282px;height:452px">
    <div class="card-media" style="height:127px;background:linear-gradient(135deg,#e3e3e3,#3b6648)" role="img" aria-label="Photo of the Corvin encoder interface board"></div>
    <h3 class="name" style="top:148px">CORVIN</h3>
    <div class="sub" style="top:182px">Universal encoder interface</div>
    <p style="top:206px">Lorem Ipsum is simply dummy text of the printing and typesetting industry. Lorem Ipsum has been the industry's standard dummy text ever since the 1500s, when an unknown printer took a galley of type and scrambled it to make a type specimen book. It has survived not only five centuries, but also the leap into electronic type-setting, remaining essentially unchanged.</p>
    <div class="btn" style="left:25px;top:406px;width:232px;height:42px;line-height:42px">READ MORE</div>
  </div>
</section>

<section class="team on-dark" role="img" aria-label="Dark photo of a cheering team in an office">
  <h2 class="section-title" style="top:38px;font-weight:400">TEAM WORK</h2>
  <div class="stat" style="left:242px;top:150px">
    <svg width="60" height="44" viewBox="0 0 60 44"><circle cx="30" cy="10" r="8" fill="#fff"/><circle cx="12" cy="16" r="6" fill="#fff"/><circle cx="48" cy="16" r="6" fill="#fff"/><path d="M16 44 a14 16 0 0 1 28 0z" fill="#fff"/><path d="M0 44 a12 14 0 0 1 18-10 v10z M60 44 a12 14 0 0 0 -18-10 v10z" fill="#fff"/></svg>
    <div class="num">1245</div><div class="label">Client</div>
  </div>
  <div class="stat" style="left:500px;top:150px">
    <svg width="44" height="44" viewBox="0 0 44 44"><path d="M4 12 h12 a5 5 0 1 1 10 0 h12 v12 a5 5 0 1 0 0 10 v10 h-34z" fill="#fff"/></svg>
    <div class="num">25468</div><div class="label">velmi</div>
  </div>
  <div class="stat" style="left:760px;top:150px">
    <svg width="52" height="44" viewBox="0 0 52 44"><circle cx="18" cy="26" r="12" fill="none" stroke="#fff" stroke-width="6" stroke-dasharray="5 3"/><circle cx="38" cy="12" r="8" fill="none" stroke="#fff" stroke-width="5" stroke-dasharray="4 2.5"/></svg>
    <div class="num">3254</div><div class="label">Completed Projects</div>
  </div>
</section>

<section class="news">
  <h2 class="col-title" style="left:133px;top:18px">NEWS</h2>
  <div class="col-rule" style="left:133px;top:60px;width:455px"></div>
  <h2 class="col-title" style="left:609px;top:18px">DUCUMENTATION</h2>
  <div class="col-rule" style="left:609px;top:60px;width:455px"></div>

  <div class="list-box" style="left:133px">
    <div class="item" style="top:16px">
      <div class="thumb" style="background:linear-gradient(135deg,#f2f6fb,#b9cbe2)" role="img" aria-label="Technical drawing thumbnail"></div>
      <h4>Lorem Ipsum is simply dummy</h4>
      <p>Lorem Ipsum is simply dummy text of the printing and typesetting industry. Lorem Ipsum has been the industry's standard dummy text ever since the 1500s, when an unknown printer took a galley of type and scrambled it to make.</p>
      <div class="more">READ MORE</div>
    </div>
    <div class="item" style="top:160px">
      <div class="thumb" style="background:linear-gradient(135deg,#d9dccf,#35573c)" role="img" aria-label="Circuit board thumbnail"></div>
      <h4>Lorem Ipsum is simply dummy</h4>
      <p>Lorem Ipsum is simply dummy text of the printing and typesetting industry. Lorem Ipsum has been the industry's standard dummy text ever since the 1500s, when an unknown printer took a galley of type and scrambled it to make.</p>
      <div class="more">READ MORE</div>
    </div>
  </div>

  <div class="list-box" style="left:609px">
    <div class="item" style="top:16px">
      <div class="thumb" style="background:linear-gradient(135deg,#f2f6fb,#b9cbe2)" role="img" aria-label="Technical drawing thumbnail"></div>
      <h4>Lorem Ipsum is simply dummy</h4>
      <p>Lorem Ipsum is simply dummy text of the printing and typesetting industry. Lorem Ipsum has been the industry's standard dummy text ever since the 1500s, when an unknown printer took a galley of type and scrambled it to make.</p>
      <div class="more">DOWNLOAD</div>
    </div>
    <div class="item" style="top:160px">
      <div class="thumb" style="background:linear-gradient(135deg,#d9dccf,#35573c)" role="img" aria-label="Circuit board thumbnail"></div>
      <h4>Lorem Ipsum is simply dummy</h4>
      <p>Lorem Ipsum is simply dummy text of the printing and typesetting industry. Lorem Ipsum has been the industry's standard dummy text ever since the 1500s, when an unknown printer took a galley of type and scrambled it to make.</p>
      <div class="more">DOWNLOAD</div>
    </div>
  </div>
</section>

<section class="contact" role="img" aria-label="Dark photo of a smiling support agent wearing a headset">
  <div class="abs center h">GET IN TOUCH</div>
  <div class="abs" style="left:447px;top:93px;width:306px;height:2px;background:#9a9a9a"></div>
  <svg class="abs" style="left:584px;top:82px" width="32" height="32" viewBox="0 0 32 32"><circle cx="16" cy="16" r="15" fill="#d6d6d6"/><path d="M11 13 l5 6 l5 -6" fill="none" stroke="#333" stroke-width="3"/></svg>

  <div class="field" style="top:172px">NAME :</div>
  <div class="field" style="top:245px">EMAIL :</div>
  <div class="field" style="top:318px">SUBJECT :</div>
  <div class="field" style="top:442px">MESSAGE :</div>
  <div class="btn" style="left:133px;top:515px;width:231px;height:43px;line-height:43px">SEND</div>

  <div class="divider"></div>
  <svg class="info-icon" style="top:180px" width="16" height="22" viewBox="0 0 16 22"><rect x="2" y="1" width="12" height="20" rx="2" fill="none" stroke="#ddd" stroke-width="2"/><circle cx="8" cy="17" r="1.5" fill="#ddd"/></svg>
  <div class="info" style="top:225px">+41 (0)26 555 01 23</div>
  <svg class="info-icon" style="top:270px" width="22" height="16" viewBox="0 0 22 16"><rect x="1" y="1" width="20" height="14" fill="none" stroke="#ddd" stroke-width="2"/><path d="M1 1 l10 8 l10 -8" fill="none" stroke="#ddd" stroke-width="2"/></svg>
  <div class="info" style="top:310px">info@velmi-example.ch</div>
  <svg class="info-icon" style="top:362px" width="22" height="18" viewBox="0 0 22 18"><path d="M1 3 l6 -2 l8 3 l6 -2 v14 l-6 2 l-8 -3 l-6 2z M7 1 v14 M15 4 v14" fill="none" stroke="#ddd" stroke-width="2"/></svg>
  <div class="info" style="top:404px">Chemin des Vergers 8</div>
  <div class="info" style="top:432px">CH - 1700 Fribourg</div>
</section>

<footer>
  <div class="copy">Copyright © 2016 · Studio Lumen</div>
  <div class="social"><span></span><span></span><span></span></div>
</footer>

</body>
</html>
```